Floor Inspections and Consulting

We provide inspections and consulting services on various floor coverings, e.g. carpet, hardwood, etc. We also do expert witness work for attorneys due to floor covering failures. We current have a logo, just need it incorporated into a new design. I have examples of cards I have found on the internet that capture my attention and make a statement. I have included our original business card, which in my opinion is terrible, but it does have our logo on it.

```html
<!DOCTYPE html>
<html lang="en">
<head>
<meta charset="utf-8">
<title>Keystone Floor Review – Business Cards</title>
<link href="https://fonts.googleapis.com/css2?family=Open+Sans:wght@400;600;700;800&display=swap" rel="stylesheet">
<style>
  :root{
    --stage:#232428;
    --navy:#07151f;
    --green:#72bf44;
    --steel:#8a98a3;
    --white:#ffffff;
    --ink:#0b1a24;
  }
  *{margin:0;padding:0;box-sizing:border-box}
  html,body{width:1200px;height:900px;overflow:hidden;background:var(--stage)}
  body{position:relative;font-family:"Open Sans",Arial,sans-serif}
  .card{position:absolute;width:700px;height:400px;overflow:hidden;border-radius:4px;box-shadow:0 18px 40px rgba(0,0,0,.45)}
  .card svg.card-art{position:absolute;inset:0;width:100%;height:100%}
  .card--contact{left:50px;top:40px}
  .card--brand{left:450px;top:470px}

  .holder-name{position:absolute;left:40px;top:120px;color:var(--white);font-weight:700;font-size:30px;letter-spacing:1px;text-transform:uppercase}
  .service-pill{position:absolute;left:395px;top:30px;background:var(--green);color:var(--navy);font-size:12px;letter-spacing:.5px;padding:3px 16px;border-radius:12px;text-transform:uppercase}

  .brand-mark{position:absolute;display:flex;align-items:center;gap:10px;color:var(--white);font-weight:700}
  .card--contact .brand-mark{left:410px;top:95px;font-size:20px;width:230px;line-height:1.15}
  .card--brand .brand-mark{left:420px;top:95px;font-size:16px;width:200px;line-height:1.15}
  .brand-dot{flex:none;border-radius:50%;background:var(--green);border:3px solid var(--white)}
  .card--contact .brand-dot{width:46px;height:46px}
  .card--brand .brand-dot{width:36px;height:36px}

  .contact-list{position:absolute;left:45px;top:275px;list-style:none;color:var(--ink);font-size:17px;line-height:27px}
  .contact-list li{display:flex;align-items:center;gap:12px}
  .contact-list svg{width:16px;height:16px;flex:none}

  .tagline{position:absolute;left:50px;top:160px;color:var(--ink);line-height:1.15}
  .tagline__lead{font-size:18px;font-weight:600}
  .tagline__main{font-size:25px;font-weight:800}

  .name-plate{position:absolute;left:330px;top:250px;border:2px solid var(--white);border-radius:12px;padding:6px 22px;font-size:38px;font-weight:700;letter-spacing:1px;text-transform:uppercase;color:var(--white)}
  .name-plate__first{color:var(--green)}
</style>
</head>
<body>

<section class="card card--contact">
  <svg class="card-art" viewBox="0 0 700 400" aria-hidden="true">
    <defs>
      <linearGradient id="steelEdge" x1="0" x2="1">
        <stop offset="0" stop-color="#07151f" stop-opacity="0"/>
        <stop offset=".5" stop-color="#8a98a3"/>
        <stop offset="1" stop-color="#3a4852"/>
      </linearGradient>
    </defs>
    <rect width="700" height="400" fill="var(--navy)"/>
    <polygon points="260,12 700,12 700,28 230,28" fill="var(--green)"/>
    <path d="M0,400 V205 C140,150 250,165 330,205 C430,255 570,250 610,170 C645,100 625,55 600,28 H700 V400 Z" fill="var(--green)"/>
    <path d="M150,170 C250,160 290,180 330,205 C430,255 570,250 610,170 C645,100 625,55 600,28" fill="none" stroke="url(#steelEdge)" stroke-width="7"/>
  </svg>
  <h1 class="holder-name">Dale Marrick</h1>
  <span class="service-pill">Analysis &amp; Consulting</span>
  <div class="brand-mark"><span class="brand-dot"></span><span>Keystone Floor Review</span></div>
  <ul class="contact-list">
    <li><svg viewBox="0 0 16 16"><circle cx="8" cy="8" r="7" fill="none" stroke="currentColor" stroke-width="1.4"/><path d="M5 4.5l1.5 0 .6 2-1 .8a5 5 0 0 0 2.6 2.6l.8-1 2 .6v1.5c-3.5.3-6.8-3-6.5-6.5z" fill="currentColor"/></svg>555-218-4470</li>
    <li><svg viewBox="0 0 16 16"><rect x="1.5" y="3.5" width="13" height="9" fill="none" stroke="currentColor" stroke-width="1.4"/><path d="M1.5 3.5L8 9l6.5-5.5" fill="none" stroke="currentColor" stroke-width="1.4"/></svg>dale@keystonefloorreview.com</li>
    <li><svg viewBox="0 0 16 16"><circle cx="8" cy="8" r="6.5" fill="none" stroke="currentColor" stroke-width="1.4"/><ellipse cx="8" cy="8" rx="3" ry="6.5" fill="none" stroke="currentColor" stroke-width="1.2"/><path d="M1.5 8h13" stroke="currentColor" stroke-width="1.2"/></svg>keystonefloorreview.com</li>
  </ul>
</section>

<section class="card card--brand">
  <svg class="card-art" viewBox="0 0 700 400" aria-hidden="true">
    <defs>
      <linearGradient id="steelEdge2" x1="0" y1="1" x2="1" y2="0">
        <stop offset="0" stop-color="#07151f" stop-opacity="0"/>
        <stop offset=".6" stop-color="#8a98a3"/>
        <stop offset="1" stop-color="#3a4852"/>
      </linearGradient>
    </defs>
    <rect width="700" height="400" fill="var(--navy)"/>
    <path d="M0,0 H580 C480,25 420,90 385,205 C355,305 300,370 190,400 H0 Z" fill="var(--green)"/>
    <path d="M580,0 C480,25 420,90 385,205 C355,305 300,370 190,400" fill="none" stroke="url(#steelEdge2)" stroke-width="8" transform="translate(6,0)"/>
  </svg>
  <p class="tagline"><span class="tagline__lead">Certified Floor Covering</span><br><span class="tagline__main">Inspections &amp; Consulting</span></p>
  <div class="brand-mark"><span class="brand-dot"></span><span>Keystone Floor Review</span></div>
  <div class="name-plate"><span class="name-plate__first">Dale</span> Marrick</div>
</section>

</body>
</html>
```